Vital Spark Electrical in need of a business card design

We need a new business card designed for our electrical business. We have a logo already which I will attach below.
Would like the business card to be..
-BLACK background preferably, possibly white back ground behind logo if colours clash.
-White & Blue (logo blue) text
Something that makes the logo pop, & a modern look. Possibly minimal clean format.

REQUIRE:
-Logo on front & back

TEXT TO INCLUDE (ON ONE SIDE):

Tom Harlow
Director/Electrician
M: 0417 365 208
E:info@vitalsparkelectrical-example.com.au
W:www.vitalsparkelectrical-example.com.au
R.E.C 57318

Custom/New Homes
Renovations
Commercial Office/Shop Fit-outs
Communications & Security Cameras
Electric Vehicle Chargers
Airconditioning
Updates

Requirements
Nice to have
• Possibly even lighten the grey shades for the words 'Vital' & 'Spark' to be more easily read on a black background.

```html
<!DOCTYPE html>
<html lang="en">
<head>
<meta charset="utf-8">
<title>Vital Spark Electrical – Business Card</title>
<link href="https://fonts.googleapis.com/css2?family=Open+Sans:ital,wght@0,400;0,600;0,700;1,700&display=swap" rel="stylesheet">
<style>
  :root {
    --stage: #2a2a2c;
    --card: #161618;
    --white: #f2f2f2;
    --grey: #c9c9cc;
    --blue: #1a9ee0;
  }
  * { margin: 0; padding: 0; box-sizing: border-box; }
  html, body { width: 1200px; height: 900px; overflow: hidden; }
  body {
    background: var(--stage);
    font-family: "Open Sans", Arial, sans-serif;
    color: var(--white);
    display: flex;
    flex-direction: column;
    align-items: center;
    justify-content: center;
    gap: 40px;
  }
  .card {
    position: relative;
    width: 700px;
    height: 400px;
    background: var(--card);
    border-radius: 4px;
    box-shadow: 0 10px 30px rgba(0,0,0,0.45);
  }
  .brand {
    display: flex;
    align-items: center;
    gap: 14px;
  }
  .brand-mark {
    width: 34px;
    height: 34px;
    background: var(--blue);
  }
  .brand-name {
    font-weight: 700;
    font-size: 30px;
    color: var(--white);
    letter-spacing: 0.5px;
  }

  /* Front */
  .card-front .brand { position: absolute; left: 56px; top: 52px; }
  .divider {
    position: absolute;
    left: 56px; right: 56px; top: 232px;
    height: 1.5px;
    background: var(--blue);
  }
  .holder {
    position: absolute;
    right: 56px; top: 160px;
    text-align: right;
  }
  .holder-name {
    font-weight: 700;
    font-style: italic;
    font-size: 26px;
    color: var(--blue);
    text-transform: uppercase;
    line-height: 1.1;
  }
  .holder-role {
    font-size: 17px;
    color: var(--white);
    margin-top: 4px;
  }
  .contacts {
    position: absolute;
    left: 56px; top: 262px;
    list-style: none;
    font-size: 16px;
    line-height: 28px;
  }
  .contacts li { display: flex; align-items: center; gap: 10px; }
  .contacts svg { width: 15px; height: 15px; flex: none; }
  .licence {
    position: absolute;
    right: 56px; bottom: 40px;
    font-size: 16px;
    color: var(--white);
  }

  /* Back */
  .card-back .brand {
    position: absolute;
    left: 0; right: 0; top: 120px;
    justify-content: center;
  }
  .card-back .brand-name { color: var(--grey); font-size: 36px; }
  .card-back .brand-mark { background: #0c0c0d; width: 40px; height: 40px; }
  .services {
    position: absolute;
    left: 0; right: 0; top: 240px;
    text-align: center;
    font-size: 16px;
    line-height: 28px;
    color: var(--white);
  }
  .services .sep { color: var(--blue); margin: 0 8px; }
</style>
</head>
<body>

  <section class="card card-front">
    <div class="brand">
      <span class="brand-mark"></span>
      <span class="brand-name">Vital Spark Electrical</span>
    </div>

    <div class="holder">
      <p class="holder-name">Tom Harlow</p>
      <p class="holder-role">Director/Electrician</p>
    </div>

    <div class="divider"></div>

    <ul class="contacts">
      <li>
        <svg viewBox="0 0 16 16" aria-hidden="true"><path fill="var(--blue)" d="M3.5 1.5l2.5 0 1 3.5-1.6 1.2a8 8 0 0 0 4.4 4.4l1.2-1.6 3.5 1v2.5a1.5 1.5 0 0 1-1.5 1.5A12.5 12.5 0 0 1 2 3a1.5 1.5 0 0 1 1.5-1.5z"/></svg>
        0417 365 208
      </li>
      <li>
        <svg viewBox="0 0 16 16" aria-hidden="true"><rect x="1" y="3" width="14" height="10" rx="1" fill="var(--blue)"/><path d="M1.5 3.8L8 9l6.5-5.2" fill="none" stroke="var(--card)" stroke-width="1.4"/></svg>
        info@vitalsparkelectrical-example.com.au
      </li>
      <li>
        <svg viewBox="0 0 16 16" aria-hidden="true"><circle cx="8" cy="8" r="6.5" fill="none" stroke="var(--blue)" stroke-width="1.5"/><ellipse cx="8" cy="8" rx="2.6" ry="6.5" fill="none" stroke="var(--blue)" stroke-width="1.2"/><path d="M1.5 8h13" stroke="var(--blue)" stroke-width="1.2"/></svg>
        www.vitalsparkelectrical-example.com.au
      </li>
    </ul>

    <p class="licence">R.E.C 57318</p>
  </section>

  <section class="card card-back">
    <div class="brand">
      <span class="brand-mark"></span>
      <span class="brand-name">Vital Spark Electrical</span>
    </div>
    <div class="services">
      <p>Custom/New Homes<span class="sep">•</span>Renovations<span class="sep">•</span>Commercial Office/Shop Fit-outs</p>
      <p>Communications &amp; Security Cameras<span class="sep">•</span>Electric Vehicle Chargers<span class="sep">•</span>Airconditioning</p>
    </div>
  </section>

</body>
</html>
```